Stationery Design Project

Would like to have the design elements we created in for our website (www.brook-holdings.example), incorporated in a stationery design layout.
Updates
Colors used in the logo attachments do not need to be used. We are open to different color variations. Looking for a crisp, clean, modern update using the design elements in attachments and which can also be viewed on or website.
A note to designers:
Project Deadline Extended
Reason: Due to update in our project description and requirements, we have decided to extend the deadline of this project to provide ample opportunity to all designers participating .
Requirements
Must have
- Must have continuity with the theme and design features used in our website. Have attached .jpg images of some of the design elements.

```html
<!DOCTYPE html>
<html lang="en">
<head>
<meta charset="utf-8">
<title>Brook Holdings Letterhead</title>
<link rel="stylesheet" href="https://fonts.googleapis.com/css2?family=PT+Sans:wght@400;700&display=swap">
<style>
  :root {
    --backdrop: #000000;
    --paper: #ffffff;
    --ink: #1f2619;
    --brand-dark: #25301f;
    --brand-green: #5cb05a;
    --band: #262d1d;
    --band-text: #ffffff;
    --rule: #3a3a3a;
  }
  * { margin: 0; padding: 0; box-sizing: border-box; }
  html, body {
    width: 850px;
    height: 1200px;
    overflow: hidden;
    background: var(--backdrop);
  }
  .letterhead {
    position: absolute;
    left: 21px;
    top: 25px;
    width: 810px;
    height: 1152px;
    background: var(--paper);
    overflow: hidden;
    font-family: "PT Sans", Arial, sans-serif;
    color: var(--ink);
  }
  .brand {
    position: absolute;
    left: 58px;
    top: 78px;
    display: flex;
    align-items: center;
    gap: 12px;
  }
  .brand-dot {
    width: 24px;
    height: 24px;
    border-radius: 50%;
    background: var(--brand-green);
  }
  .brand-name {
    font-size: 44px;
    font-weight: 700;
    color: var(--brand-dark);
    line-height: 1;
    letter-spacing: 0.2px;
  }
  .divider {
    position: absolute;
    left: 570px;
    top: 39px;
    width: 1px;
    height: 141px;
    background: var(--rule);
  }
  .contact {
    position: absolute;
    left: 591px;
    top: 38px;
    font-size: 15px;
    line-height: 21px;
    letter-spacing: -0.2px;
    color: var(--ink);
    font-style: normal;
  }
  .contact .company { font-weight: 700; }
  .contact .email-label { margin-top: 21px; }
  .footer-band {
    position: absolute;
    left: 0;
    right: 0;
    bottom: 0;
    height: 49px;
    background: var(--band);
    display: flex;
    align-items: center;
    padding-left: 34px;
  }
  .website {
    color: var(--band-text);
    font-size: 15px;
    letter-spacing: 3.2px;
  }
  .corner-mark {
    position: absolute;
    left: 560px;
    top: 978px;
    width: 220px;
    height: 220px;
    border-radius: 50%;
    background: var(--brand-green);
  }
</style>
</head>
<body>
  <main class="letterhead">
    <header>
      <div class="brand">
        <span class="brand-dot"></span>
        <span class="brand-name">Brook Holdings.inc</span>
      </div>
      <div class="divider"></div>
      <address class="contact">
        <div class="company">Brook Holdings, Inc.</div>
        <div>418 Alder Creek Road Suite 120</div>
        <div>Milltown, GA 30999</div>
        <div>PHONE: (555) 014-2233</div>
        <div>FAX: (555) 014-2299</div>
        <div class="email-label">E-mail us:</div>
        <div>info@brook-holdings.example</div>
      </address>
    </header>
    <footer class="footer-band">
      <span class="website">www.brook-holdings.example</span>
    </footer>
    <div class="corner-mark" role="img" aria-label="Large green brand decoration in the lower right corner"></div>
  </main>
</body>
</html>
```